Website for a Psychologist in Private Practice

I need a cool web design for my website: www.drvalporte.com. I would like it to look professional. Keep all the current content and add: Space for video; radio spots (see Silver Harbor Tunes Logo below for those); Quick Inquiry; Chatterbook link; 5 star rating on Rivo; a map; reviews from former patients. I am open to suggestions.

Target Market(s)

Those seeking individual and marital counseling.

Industry/Entity Type

Mental Health

Number of Pages Required

1 page

Font styles to use
Sans Serif
Other font styles liked:
• I'm open but no hard to read script

Requirements
Must have
• All the content on my home page with link for video and radio spots. List services and degrees and expertices (pics not necessary).
Nice to have
• A video of me and radio conversations (logo of Silver Harbor Tunes radio attached).
Should not have
• Cartoons, comedy, etc.... I don't need pictures of services (marital, depression, etc...) Just list those.

```html
<!DOCTYPE html>
<html lang="en">
<head>
<meta charset="utf-8">
<title>Dr. Dana Z. Valporte — Clinical Psychologist</title>
<link href="https://fonts.googleapis.com/css2?family=Open+Sans:ital,wght@0,300;0,400;0,600;0,700;1,400&family=Playfair+Display+SC:wght@700&display=swap" rel="stylesheet">
<style>
:root{
  --water-deep:#3f7fb6;
  --water-mid:#6fa3cf;
  --water-light:#a9c9e4;
  --panel:rgba(214,230,244,0.72);
  --band:rgba(226,237,247,0.9);
  --ink:#1f2a36;
  --ink-soft:#2f3d4c;
  --accent:#2f6fb2;
  --sidebar:#262626;
  --sidebar-text:#d6d6d6;
  --sidebar-muted:#8a8a8a;
  --footer:#2b2b2b;
  --white:#ffffff;
  --button:#1f6fd0;
}
*{box-sizing:border-box;margin:0;padding:0}
html,body{width:710px;height:1200px;overflow:hidden}
body{
  position:relative;font-family:"Open Sans",sans-serif;color:var(--ink);
  background:
    repeating-linear-gradient(172deg,rgba(255,255,255,0.06) 0 6px,rgba(0,0,0,0.04) 6px 14px),
    linear-gradient(180deg,var(--water-deep) 0%,var(--water-mid) 45%,var(--water-light) 75%,var(--water-mid) 100%);
}
.abs{position:absolute}
.nav{top:14px;right:85px;display:flex;gap:22px;font-size:8.5px;font-weight:600;color:var(--white);letter-spacing:.3px}
.nav a{color:inherit;text-decoration:none}
.brand{left:44px;top:48px;width:302px}
.brand-name{font-family:"Playfair Display SC",serif;font-size:25px;color:var(--ink);letter-spacing:.2px;line-height:1;border-bottom:1px solid var(--ink);padding-bottom:3px}
.brand-address{font-size:7.5px;letter-spacing:2.2px;border-bottom:1px solid var(--ink);padding:3px 0 3px}
.brand-contact{font-size:8.5px;margin-top:4px;display:flex;gap:10px;align-items:center}
.brand-contact span{display:flex;align-items:center;gap:3px}
.content-panel{left:44px;top:152px;width:621px;height:536px;background:var(--panel)}
.main{left:97px;top:190px;width:303px;font-size:7.4px;line-height:13.5px;color:var(--ink-soft)}
.main h1{font-weight:300;font-size:17px;color:var(--ink);margin-bottom:14px}
.main h2{font-family:"Playfair Display SC",serif;font-size:13px;color:var(--ink);margin:21px 0 12px}
.main p{margin-bottom:13px}
.main blockquote{border-left:3px solid var(--accent);padding-left:10px;font-weight:700;color:var(--ink);margin-bottom:13px}
.sidebar{left:417px;top:57px;width:195px;height:631px;background:var(--sidebar);color:var(--sidebar-text)}
.portrait{position:absolute;left:14px;top:18px;width:167px;height:192px;background:linear-gradient(160deg,#5c7a3a,#c9b48a 45%,#3c6fa8);border:1px solid #111}
.side-inner{position:absolute;left:14px;top:221px;width:170px;font-size:7.4px;line-height:13px}
.side-title{font-size:10px;letter-spacing:1.4px;color:var(--white)}
.side-license{color:var(--sidebar-muted);font-size:7.4px}
.rule{width:14px;height:2px;background:#666;margin:10px 0 14px}
.badge-verified{width:80px;height:17px;background:#e9e9e9;border:1px solid #999;margin:12px 0 20px}
.side-heading{font-family:"Playfair Display SC",serif;font-size:10px;color:var(--white);margin-bottom:8px}
.side-list li{list-style:none;line-height:16.5px}
.testimonial-band{left:0;top:688px;width:710px;height:146px;background:var(--band)}
.avatar{left:331px;top:702px;width:48px;height:48px;border-radius:50%;background:linear-gradient(#c9ad96,#6c5a4c);border:2px solid #fff}
.quote{left:140px;top:753px;width:430px;text-align:center;font-style:italic;font-size:7.2px;line-height:12px;color:#2a3f5e}
.quote-rule{left:349px;top:797px;width:12px;height:1px;background:var(--accent)}
.quote-name{left:255px;top:803px;width:200px;text-align:center;font-size:7.8px;color:var(--ink-soft)}
.arrow{top:748px}
.section-heading{top:864px;font-family:"Playfair Display SC",serif;font-size:10px;color:var(--ink)}
.video{left:44px;top:880px;width:249px;height:142px;background:#222}
.video-still{position:absolute;left:0;top:0;width:249px;height:123px;background:linear-gradient(90deg,#2c4a15,#5b8a2a 45%,#c8a882 70%,#3f73ad)}
.video-bar{position:absolute;left:0;top:123px;width:249px;height:19px;background:#2b2b2b}
.form{left:310px;top:879px;width:196px;height:141px;background:rgba(196,213,229,0.9);border:1px solid #e5eef7}
.field{position:absolute;background:#fff;font-size:6px;color:#9aa8b6;padding:3px 4px;font-style:italic}
.send{position:absolute;left:15px;top:111px;width:60px;height:15px;background:var(--button);color:#fff;font-size:6.5px;font-weight:700;text-align:center;line-height:15px}
.radio-spot{left:524px;top:880px;width:141px;height:141px;background:linear-gradient(160deg,#e3306c,#8a5a60 45%,#2a2a2a)}
.radio-title{position:absolute;left:0;top:3px;width:141px;text-align:center;font-size:10px;font-weight:600;color:#fff}
.radio-time{position:absolute;left:4px;bottom:6px;font-size:6.5px;font-weight:600;color:#fff;line-height:9px}
.footer{left:0;top:1060px;width:710px;height:140px;background:var(--footer);color:#e5e5e5}
.foot-col{position:absolute;text-align:center;font-size:6.8px;line-height:9.5px}
.vsep{position:absolute;top:22px;width:1px;height:56px;background:#444}
.partner{display:inline-block;width:54px;height:18px;margin:0 1px}
.rating{width:90px;height:27px;background:#c4161c;color:#fff;font-size:8px;font-weight:600;line-height:27px;margin:6px auto 0}
.map{position:absolute;left:329px;top:25px;width:158px;height:76px;background:linear-gradient(135deg,#e8e8e8,#d9dde2);border:2px solid #fff}
.map span{position:absolute;left:5px;bottom:3px;font-size:6px;font-style:italic;color:#333}
.contact-col{position:absolute;left:520px;top:28px;width:160px;text-align:center}
.socials{display:flex;justify-content:center;gap:6px;font-size:6.5px;color:#ccc;margin-bottom:4px}
.socials span{display:flex;align-items:center;gap:3px}
.socials i{width:8px;height:8px;background:#3b6fb4;display:inline-block}
.foot-phone{font-size:15px;color:#fff;display:flex;justify-content:center;align-items:center;gap:4px}
.foot-address{font-size:6.8px;line-height:10px;margin-top:5px}
.foot-email{font-size:8.5px;margin-top:6px}
.copyright{position:absolute;left:0;top:124px;width:710px;text-align:center;font-size:6.2px}
</style>
</head>
<body>

<nav class="abs nav"><a href="#">HOME</a><a href="#">SESSIONS</a><a href="#">RESOURCES</a><a href="#">BIO</a><a href="#">CONTACT</a></nav>

<header class="abs brand">
  <div class="brand-name">Dr. Dana Z. Valporte</div>
  <div class="brand-address">417 LINDEN STREET, SUITE 210 HARBOR COVE, CA 90412</div>
  <div class="brand-contact">
    <span><svg width="8" height="8" viewBox="0 0 10 10"><circle cx="5" cy="5" r="4.3" fill="none" stroke="#1f2a36" stroke-width="1"/><path d="M3.5 3l1 1-.5.7 1.3 1.3.7-.5 1 1-.7.8C4.5 7 3 5.5 2.7 3.7z" fill="#1f2a36"/></svg>(555) 318 4420</span>
    <span><svg width="9" height="7" viewBox="0 0 10 8"><rect x=".5" y=".5" width="9" height="7" fill="none" stroke="#1f2a36"/><path d="M.5 .5l4.5 4 4.5-4" fill="none" stroke="#1f2a36"/></svg>dv@drvalporte.com</span>
  </div>
</header>

<div class="abs content-panel"></div>

<main class="abs main">
  <h1>Your quality of life is Important.</h1>
  <p>Choosing to see a professional for issues in your life can be difficult but also possibly life changing. Many postpone seeking help because they believe doing so acknowledges failure on their part.</p>
  <blockquote>Really? We seek the help of experts all the time (contractors, mechanics, chefs, etc..) and what is more important than your life?</blockquote>
  <p>Consulting with a neutral party to act in your best interest can be time well spent. So if you are willing to take the time to invest in counseling, make sure that it is with someone that is worth your time.</p>
  <h2>Do Not Compromise</h2>
  <p>Choose a licensed psychologist with a doctoral degree (Ph.D. or PsyD.) - both have over 10 years of education in the field of psychology, extensive internships and comprehensive licensing exams. Others have far less education if any. Also, consider the therapist's approach to therapy. I use a straightforward approach (<i>psychobabble available upon request</i>) with brief, solution-oriented sessions.</p>
  <p>Experience also separates good psychologists from others with fewer and more proficient sessions. My 20+ years of professional experience and my life experience contributes to the empathetic perspective I use to relate to each person I see. I also believe it is the reason 90% of my practice is referral based and why many other psychologists in the area seek my services.</p>
  <blockquote>Experience separates good psychologists from others with fewer and more proficient sessions.</blockquote>
  <p>Find an educated, licensed, experienced professional that you can relate to. Think about what it took to get you here and the importance resolving this issue can have on your life.</p>
</main>

<aside class="abs sidebar">
  <div class="portrait" role="img" aria-label="Portrait photograph of Dr. Valporte"></div>
  <div class="side-inner">
    <div class="side-title">CLINICAL PSYCHOLOGIST</div>
    <div class="side-license">California # PSY20581</div>
    <div class="rule"></div>
    <div>Doctoral Degree in Clinical Psychology<br>Masters Degree in Counseling Psychology<br>Doctoral Internship, Harbor University Medical Center<br>Masters Internship, Linden Clinic</div>
    <div class="badge-verified" role="img" aria-label="Directory verification badge"></div>
    <div class="side-heading">Expertise</div>
    <ul class="side-list"><li>Dating &amp; Marriage</li><li>Parenting &amp; Professional Relationships</li><li>Depression &amp; Anxiety Issues</li><li>Personality Disorders</li><li>Life Management</li></ul>
    <div class="rule"></div>
    <div class="side-heading">Services</div>
    <ul class="side-list"><li>Individual &amp; Group Counseling</li><li>Couple / Family Therapy</li><li>Stress Management</li><li>Psychological Testing</li></ul>
  </div>
</aside>

<section class="abs testimonial-band"></section>
<div class="abs avatar" role="img" aria-label="Reviewer photo"></div>
<svg class="abs arrow" style="left:44px" width="14" height="24" viewBox="0 0 14 24"><path d="M12 2L3 12l9 10" fill="none" stroke="#7aaad6" stroke-width="3"/></svg>
<svg class="abs arrow" style="left:652px" width="14" height="24" viewBox="0 0 14 24"><path d="M2 2l9 10-9 10" fill="none" stroke="#7aaad6" stroke-width="3"/></svg>
<p class="abs quote">“I have had other counseling experiences, however, I have never made such significant strides until I met Dr. Valporte. I feel so fortunate to have found her. She is a true professional who is both compassionate and incredibly effective. Wonderful person, she has made my life so much better.”</p>
<div class="abs quote-rule"></div>
<div class="abs quote-name">Mr. JN, Bayview</div>

<h3 class="abs section-heading" style="left:44px">Videos</h3>
<h3 class="abs section-heading" style="left:310px">Get In Touch</h3>
<h3 class="abs section-heading" style="left:524px">Conversations</h3>

<div class="abs video">
  <div class="video-still" role="img" aria-label="Video still of the talk show with Dr. Valporte"></div>
  <svg style="position:absolute;left:110px;top:44px" width="30" height="30" viewBox="0 0 30 30"><circle cx="15" cy="15" r="15" fill="rgba(255,255,255,0.45)"/><path d="M12 9l9 6-9 6z" fill="#fff"/></svg>
  <div class="video-bar">
    <svg width="249" height="19" viewBox="0 0 249 19"><path d="M8 5l7 4.5-7 4.5z" fill="#fff"/><rect x="22" y="8" width="120" height="3" fill="#999"/><rect x="22" y="8" width="10" height="3" fill="#1f6fd0"/><text x="149" y="12" font-size="5.5" fill="#ddd" font-family="Open Sans,sans-serif">0:04 / 20:30</text><path d="M180 7h3l3-3v11l-3-3h-3z" fill="#fff"/><rect x="191" y="8" width="52" height="3" fill="#1f6fd0"/></svg>
  </div>
</div>

<form class="abs form">
  <div class="field" style="left:15px;top:20px;width:101px;height:15px">Name</div>
  <div class="field" style="left:15px;top:43px;width:75px;height:15px">Email</div>
  <div class="field" style="left:107px;top:43px;width:75px;height:15px">Phone#</div>
  <div class="field" style="left:15px;top:67px;width:167px;height:34px">Message</div>
  <div class="send">SEND</div>
</form>

<div class="abs radio-spot" role="img" aria-label="Silver Harbor Tunes radio show artwork with hosts">
  <div class="radio-title">Silver Harbor Tunes</div>
  <div class="radio-time">SUNDAYS<br>4PM PST/7PM EST<br>WAVELINE RADIO</div>
</div>

<footer class="abs footer">
  <div class="foot-col" style="left:50px;top:46px;width:132px">A portion of all revenue is<br>donated to
    <div style="margin-top:6px"><span class="partner" style="background:#fff"></span><span class="partner" style="background:#5b7f2e"></span></div>
  </div>
  <div class="vsep" style="left:187px"></div>
  <div class="foot-col" style="left:200px;top:46px;width:98px">Read Reviews
    <div class="rating">5 star rated · Rivo</div>
  </div>
  <div class="vsep" style="left:310px"></div>
  <div class="map" role="img" aria-label="Street map of the office location"><span>click to enlarge</span></div>
  <div class="vsep" style="left:506px"></div>
  <div class="contact-col">
    <div class="socials"><span><i></i>Chatterbook</span><span><i></i>Linkdeck</span></div>
    <div class="foot-phone"><svg width="13" height="13" viewBox="0 0 10 10"><circle cx="5" cy="5" r="4.3" fill="none" stroke="#fff" stroke-width=".9"/><path d="M3.5 3l1 1-.5.7 1.3 1.3.7-.5 1 1-.7.8C4.5 7 3 5.5 2.7 3.7z" fill="#fff"/></svg>555.318.4420</div>
    <div class="foot-address">417 Linden Street, Suite 210<br>Harbor Cove, CA 90412</div>
    <div class="foot-email">✉&nbsp; dv@drvalporte.com</div>
  </div>
  <div class="copyright">© Dr Dana Valporte 2016 All Rights Reserved</div>
</footer>

</body>
</html>
```